Wine labels Velmora Wine Council - Nueva etiqueta El Consejo Regulador de vinos de Albarrán

Velmora Wines Council, based in southern Spain, are looking to create a new suite of wine labels which retain the elegance of the Velmora Wines industry while reinvigorating their image to the modern era and a new generation of Sherry Wine lovers. These labels will be used across the Velmora Wines Council's range of wines for the promotion of the Velmora Wines industry.

Your design must present at least two styles of Velmora Wines which demonstrate an elegant, modern interpretation and understanding of the unique mood and personality for these wines and the essence of southern Spain.

10 labels will be created based on the winning design, one for each of the unique varieties of Velmora Wines within the collection. This collection comprises of several different wine varieties including: Fino, Manzanilla, Amontillado, Oloroso, Palo Cortado, Medium, Cream, Pale Cream, Pedro Ximenez and Moscatel.

We recommend you visit our website www.velmora-vinos.example/wines as the source to understanding the origins and unique personality of these diverse wines.

El Consejo Regulador de los Vinos de Albarrán y Tordesal quiere renovar las etiquetas de los vinos utilizados para sus actividades de promoción genérica. Esta colección de vinos comprende las tipologías más importantes de la región que incluye: fino, manzanilla, amontillado, oloroso, palo cortado, pale cream, medium, cream, pedro ximénez y moscatel. Por lo tanto se precisan 10 etiquetas, una para cada uno de los vinos mencionados.
Updates

Project Deadline Extended
Reason: Due to some confusion with the deadline we wish to officially extend the deadline to allow designers one last week to submit their entries.

Target Market(s)

Industry, journalists, media, sommeliers, chefs, wine writers

Industry/Entity Type

Council

Requirements
Must have
• Front and Back label plus capsule:
• Front label can have either of the two official logos of the Velmora Wine council titled Vinos de Albarrán Digital or not, this is optional. Must include: Vino selecionado por el Consejo Regulador de la Denominacion de Origen, Name of the variety of wine eg FINO, percentage of alcohol eg 15% and quantity 75 cl.
• The back of the label must include the council logo titled Sellora and 4 additional logos positioned smaller. The Europa logo must appear larger than the 3 other logos. Space for descriptive text about the wine is also required.
• The dimensions of the bottle can be found at this link http://www.vidrialto.example/es/catalogo/vinos-y-espumosos/bordelesas/bd-orla
• Altura:305 mm
• Diámetro base:76,20 mm
• Diámetro hombro:82 mm
• Tipo boca:Cetie
• Peso:750 gr
• Capacidad:75 cl
• Etiqueta delantera y trasera y capsula
• La etiqueta delantera puede incluir el logo oficial del Consejo Regulador o el logo digital, o ninguno, esto es opcional. Debe incluir el siguiete texto: Vino selecionado por el Consejo Regulador de la Denominacion de Origen, el nombre de la variedad del vino, por ejemplo Fino, el porcentaje de alcohol, por ejemplo 15%, y la capacidad 75cl.
• La etiqueta trasera debe incluir el logo oficial Sellora del Consejo, y cuatro logos adicionales con una dimension menor. El Logo de ¨Europa invierte en las zonas rurales¨ debe ser de mayor tamaño que los otros. Se precisa espacio para el texto descriptivo de los vinos.
• Las dimensiones de la botella se puede encontrar en este enlace
• http://www.vidrialto.example/es/catalogo/vinos-y-espumosos/bordelesas/bd-orla
• Altura:305 mm
• Diámetro base:76,20 mm
• Diámetro hombro:82 mm
• Tipo boca:Cetie
• Peso:750 gr
• Capacidad:75 cl
Nice to have
• See our website velmora-vinos.example to understand the origin of the wines. Ver nuestra página web velmora-vinos.example para mejor entender los vinos.
Should not have
• Images of catavinos or stereotypical images from Spain such as flamenco dancers or guitars.

```html
<!DOCTYPE html>
<html lang="es">
<head>
<meta charset="utf-8">
<title>Velmora Wines – etiquetas</title>
<link rel="stylesheet" href="https://fonts.googleapis.com/css2?family=Bodoni+Moda:wght@400;500&display=swap">
<style>
  :root {
    --paper: #ffffff;
    --band: #e1a832;
    --gold: #f2cc5e;
    --ink-dark: #3a1a0c;
    --ink-red: #7a1a10;
    --band-light-text: #f7d774;
    --pedro: #2a1c14;
    --amontillado: #783617;
    --palo: #611b0e;
    --manzanilla: #f8e585;
    --fino: #f8d648;
    --oloroso: #561c0e;
    --medium: #8e4420;
    --cream: #391410;
    --palecream: #54262a;
    --moscatel: #5d2a24;
  }
  * { margin: 0; padding: 0; box-sizing: border-box; }
  html, body { width: 1200px; height: 852px; overflow: hidden; background: var(--paper); }
  .sheet { position: relative; width: 1200px; height: 852px; font-family: "Bodoni Moda", "Bodoni 72", serif; }

  .label {
    position: absolute; width: 177px; height: 354px;
    background: var(--bg); color: var(--text);
    --text: var(--gold); --band-text: var(--ink-dark);
  }
  .label--light { --text: var(--ink-red); --band-text: var(--band-light-text); }

  .label__variety {
    position: absolute; top: 44px; left: 0; width: 133px; height: 44px;
    background: var(--band); color: var(--band-text);
    font-size: 10.5px; letter-spacing: 0.3px; padding: 8px 0 0 44px;
  }
  .label__mark {
    position: absolute; top: 150px; left: 50%; width: 30px; height: 30px;
    margin-left: -15px; border: 1.5px solid var(--text); border-radius: 50%;
  }
  .label__brand {
    position: absolute; top: 218px; left: 0; width: 100%; text-align: center;
    font-size: 10.5px; letter-spacing: 1.6px;
  }
  .label__statement {
    position: absolute; top: 270px; right: 44px; text-align: right;
    font-size: 6.6px; line-height: 8.6px; white-space: nowrap;
  }
  .label__rule {
    position: absolute; top: 310px; right: 44px; width: 21px; height: 0;
    border-top: 0.8px solid var(--text); opacity: 0.8;
  }
  .label__specs {
    position: absolute; top: 323px; right: 44px; text-align: right;
    font-size: 6.6px; line-height: 8px;
  }

  .col-1 { left: 25px; } .col-2 { left: 271px; } .col-3 { left: 515px; }
  .col-4 { left: 756px; } .col-5 { left: 1004px; }
  .row-1 { top: 25px; } .row-2 { top: 469px; }

  .v-pedro { --bg: var(--pedro); }
  .v-amontillado { --bg: var(--amontillado); }
  .v-palo { --bg: var(--palo); }
  .v-manzanilla { --bg: var(--manzanilla); }
  .v-fino { --bg: var(--fino); }
  .v-oloroso { --bg: var(--oloroso); }
  .v-medium { --bg: var(--medium); }
  .v-cream { --bg: var(--cream); }
  .v-palecream { --bg: var(--palecream); }
  .v-moscatel { --bg: var(--moscatel); }
</style>
</head>
<body>
<main class="sheet">

  <article class="label v-pedro row-1 col-1">
    <div class="label__variety">pedro ximenez</div>
    <div class="label__mark"></div>
    <div class="label__brand">VELMORA WINES</div>
    <p class="label__statement">Vino selecionado por<br>el Consejo Regulador de la<br>Denominacion de Origen</p>
    <div class="label__rule"></div>
    <p class="label__specs">75 cl<br>Alc: 15%</p>
  </article>

  <article class="label v-amontillado row-1 col-2">
    <div class="label__variety">amontillado</div>
    <div class="label__mark"></div>
    <div class="label__brand">VELMORA WINES</div>
    <p class="label__statement">Vino selecionado por<br>el Consejo Regulador de la<br>Denominacion de Origen</p>
    <div class="label__rule"></div>
    <p class="label__specs">75 cl<br>Alc: 15%</p>
  </article>

  <article class="label v-palo row-1 col-3">
    <div class="label__variety">palo cortado</div>
    <div class="label__mark"></div>
    <div class="label__brand">VELMORA WINES</div>
    <p class="label__statement">Vino selecionado por<br>el Consejo Regulador de la<br>Denominacion de Origen</p>
    <div class="label__rule"></div>
    <p class="label__specs">75 cl<br>Alc: 15%</p>
  </article>

  <article class="label label--light v-manzanilla row-1 col-4">
    <div class="label__variety">manzanilla</div>
    <div class="label__mark"></div>
    <div class="label__brand">VELMORA WINES</div>
    <p class="label__statement">Vino selecionado por<br>el Consejo Regulador de la<br>Denominacion de Origen</p>
    <div class="label__rule"></div>
    <p class="label__specs">75 cl<br>Alc: 15%</p>
  </article>

  <article class="label label--light v-fino row-1 col-5">
    <div class="label__variety">fino</div>
    <div class="label__mark"></div>
    <div class="label__brand">VELMORA WINES</div>
    <p class="label__statement">Vino selecionado por<br>el Consejo Regulador de la<br>Denominacion de Origen</p>
    <div class="label__rule"></div>
    <p class="label__specs">75 cl<br>Alc: 15%</p>
  </article>

  <article class="label v-oloroso row-2 col-1">
    <div class="label__variety">oloroso</div>
    <div class="label__mark"></div>
    <div class="label__brand">VELMORA WINES</div>
    <p class="label__statement">Vino selecionado por<br>el Consejo Regulador de la<br>Denominacion de Origen</p>
    <div class="label__rule"></div>
    <p class="label__specs">75 cl<br>Alc: 15%</p>
  </article>

  <article class="label v-medium row-2 col-2">
    <div class="label__variety">medium</div>
    <div class="label__mark"></div>
    <div class="label__brand">VELMORA WINES</div>
    <p class="label__statement">Vino selecionado por<br>el Consejo Regulador de la<br>Denominacion de Origen</p>
    <div class="label__rule"></div>
    <p class="label__specs">75 cl<br>Alc: 15%</p>
  </article>

  <article class="label v-cream row-2 col-3">
    <div class="label__variety">cream</div>
    <div class="label__mark"></div>
    <div class="label__brand">VELMORA WINES</div>
    <p class="label__statement">Vino selecionado por<br>el Consejo Regulador de la<br>Denominacion de Origen</p>
    <div class="label__rule"></div>
    <p class="label__specs">75 cl<br>Alc: 15%</p>
  </article>

  <article class="label v-palecream row-2 col-4">
    <div class="label__variety">pale cream</div>
    <div class="label__mark"></div>
    <div class="label__brand">VELMORA WINES</div>
    <p class="label__statement">Vino selecionado por<br>el Consejo Regulador de la<br>Denominacion de Origen</p>
    <div class="label__rule"></div>
    <p class="label__specs">75 cl<br>Alc: 15%</p>
  </article>

  <article class="label v-moscatel row-2 col-5">
    <div class="label__variety">moscatel</div>
    <div class="label__mark"></div>
    <div class="label__brand">VELMORA WINES</div>
    <p class="label__statement">Vino selecionado por<br>el Consejo Regulador de la<br>Denominacion de Origen</p>
    <div class="label__rule"></div>
    <p class="label__specs">75 cl<br>Alc: 15%</p>
  </article>

</main>
</body>
</html>
```